Dog care service needs business card design

Our company is Paws Harbour. We provide care for dogs while their owners are away, either through home visits or a holiday stay in the homes of carefully selected minders. Our existing website & Chatterbook cover should provide all the colour cues for our business cards - namely blues, blondes and grey. We have an existing logo (provided).

www.pawsharbourcare.example.au
www.facebook.com/pawsharbourcareau

We wish to clearly communicate our three areas of service "dog minding, home visits, dog walking".

We would like to have the files ready for upload to Printlyne (or similar) for immediate printing.

Target Market(s)

Dog owners who love their dogs like family

Industry/Entity Type

Business

Contact Information for Business Card

Paws Harbour
Ph: 0417 358 904

Font styles to use
Sans Serif

Colors
33a6d7
3176b5

Requirements
Must have
• Logo
• Telephone number
• website
• "Dog minding, home visits, dog walking"
Should not have
• any additional illustrations beyond the logo.

```html
<!DOCTYPE html>
<html lang="en">
<head>
<meta charset="utf-8">
<title>Paws Harbour – Business Cards</title>
<link rel="stylesheet" href="https://fonts.googleapis.com/css2?family=Arimo:wght@400;500&display=swap">
<style>
  :root {
    --stage: #e9ebee;
    --card: #ffffff;
    --ink: #4a5566;
    --ink-soft: #5d6878;
    --blue: #33a6d7;
    --blue-deep: #3176b5;
    --divider: #5d6878;
  }
  * { box-sizing: border-box; margin: 0; padding: 0; }
  html, body {
    width: 1200px; height: 914px; overflow: hidden;
    background: var(--stage);
    font-family: "Arimo", Arial, sans-serif;
    color: var(--ink);
  }
  .sheet {
    width: 1200px; height: 914px;
    display: flex; flex-direction: column;
    align-items: center; justify-content: center; gap: 60px;
  }
  .card {
    position: relative;
    width: 640px; height: 366px;
    background: var(--card);
    box-shadow: 0 6px 20px rgba(40, 50, 70, 0.14);
    overflow: hidden;
  }

  /* Brand mark (name set as text) */
  .brand { display: flex; align-items: center; gap: 12px; }
  .brand-dot {
    width: 16px; height: 16px; border-radius: 50%;
    background: var(--blue); flex: none;
  }
  .brand-name {
    font-weight: 400; color: var(--ink);
    letter-spacing: 0.5px; white-space: nowrap;
  }

  /* Contact side */
  .brand-panel {
    position: absolute; left: 40px; top: 110px; width: 290px;
  }
  .card--info .brand-name { font-size: 30px; }
  .services {
    margin-top: 18px;
    font-size: 14px; color: var(--ink); white-space: nowrap;
  }
  .divider {
    position: absolute; left: 350px; top: 60px;
    width: 1.5px; height: 246px; background: var(--divider);
  }
  .person { position: absolute; left: 376px; top: 82px; }
  .person-name { font-size: 24px; color: var(--ink); line-height: 1; white-space: nowrap; }
  .person-role { font-size: 15px; color: var(--ink); margin-top: 5px; white-space: nowrap; }

  .contacts {
    position: absolute; left: 376px; top: 158px; width: 250px;
    list-style: none; font-size: 13px; color: var(--ink-soft);
  }
  .contacts li {
    display: flex; align-items: flex-start; gap: 9px;
    line-height: 17px; margin-bottom: 8px; white-space: nowrap;
  }
  .contacts svg { width: 15px; height: 15px; flex: none; margin-top: 1px; fill: var(--blue); }

  /* Logo side */
  .card--logo .brand { position: absolute; right: 60px; bottom: 70px; }
  .card--logo .brand-name { font-size: 44px; }
</style>
</head>
<body>
<main class="sheet">

  <section class="card card--logo" aria-label="Card back with brand name">
    <div class="brand">
      <span class="brand-dot"></span>
      <span class="brand-name">Paws Harbour</span>
    </div>
  </section>

  <section class="card card--info" aria-label="Card front with contact details">
    <div class="brand-panel">
      <div class="brand">
        <span class="brand-dot"></span>
        <span class="brand-name">Paws Harbour</span>
      </div>
      <p class="services">Dog minding | home visits | dog walking</p>
    </div>

    <div class="divider"></div>

    <div class="person">
      <p class="person-name">Employee Name</p>
      <p class="person-role">Managing Director</p>
    </div>

    <ul class="contacts">
      <li>
        <svg viewBox="0 0 16 16" aria-hidden="true"><circle cx="8" cy="5" r="3.4"/><path d="M1.5 15c0-3.6 2.9-5.6 6.5-5.6s6.5 2 6.5 5.6z"/></svg>
        <span>0417 358 904</span>
      </li>
      <li>
        <svg viewBox="0 0 16 16" aria-hidden="true"><path d="M8 1a7 7 0 1 0 0 14A7 7 0 0 0 8 1zm0 1.5c.8 0 1.8 1.7 2.1 4.3H5.9C6.2 4.2 7.2 2.5 8 2.5zM2.6 7.3h2.3c0 .5 0 1 .1 1.4H2.6a5.6 5.6 0 0 1 0-1.4zm.4 2.9h2.2c.2 1.2.6 2.2 1 2.9A5.5 5.5 0 0 1 3 10.2zm5 3.3c-.8 0-1.6-1.3-2-3.3h4c-.4 2-1.2 3.3-2 3.3zm2.8-.4c.4-.7.8-1.7 1-2.9H13a5.5 5.5 0 0 1-2.2 2.9zm.2-4.4c.1-.4.1-.9.1-1.4h2.3a5.6 5.6 0 0 1 0 1.4z"/></svg>
        <span>www.pawsharbourcare.example.au</span>
      </li>
      <li>
        <svg viewBox="0 0 16 16" aria-hidden="true"><path d="M1 3h14v10H1zm1.4 1.3L8 8.6l5.6-4.3zM2.3 12h11.4V5.6L8 10 2.3 5.6z"/></svg>
        <span>info@pawsharbourcare.example.au</span>
      </li>
      <li>
        <svg viewBox="0 0 16 16" aria-hidden="true"><path d="M8 0.8a5 5 0 0 0-5 5c0 3.8 5 9.4 5 9.4s5-5.6 5-9.4a5 5 0 0 0-5-5zm0 7a2 2 0 1 1 0-4 2 2 0 0 1 0 4z"/></svg>
        <span>Ferndale Heights, New South Wales<br>Australia 2790</span>
      </li>
    </ul>
  </section>

</main>
</body>
</html>
```